Wellness product startup company needs packing design

We are starting up with a range of wellness products and looking for colorful, modern & trendy designs, highlighting the brand and product name as bold & prominent as possible.
sending few samples which I tried to design myself. not at all happy with the result though.
Also please use colors that go well with the Health & Wellness products (these products also comes under food supplement range)
Target Market(s)
India
Industry/Entity Type
Health And Wellness
Font styles to use
Serif
Colors
9bcb3b
f37122
e34197
Requirements
Must have
- Prominent logo & product name
Nice to have
- I leave it to you.
Should not have
- I leave it to designer.

```html
<!DOCTYPE html>
<html lang="en">
<head>
<meta charset="utf-8">
<title>Verdana Roots – Vigor+ Label</title>
<link rel="stylesheet" href="https://fonts.googleapis.com/css2?family=Arimo:wght@400;700&display=swap">
<style>
  :root {
    --crimson: #cf1f5d;
    --leaf: #8cbf3a;
    --paper: #ffffff;
    --ink: #1f1f1f;
    --backdrop: #eeeeee;
  }
  * { margin: 0; padding: 0; box-sizing: border-box; }
  html, body {
    width: 1200px;
    height: 1000px;
    overflow: hidden;
    background: var(--backdrop);
    font-family: "Arimo", Arial, sans-serif;
  }
  .label {
    position: absolute;
    left: 330px;
    top: 200px;
    width: 540px;
    height: 600px;
  }
  .label-art {
    position: absolute;
    inset: 0;
    width: 540px;
    height: 600px;
  }
  .brand {
    position: absolute;
    top: 150px;
    left: 0;
    width: 540px;
    display: flex;
    justify-content: center;
    align-items: center;
    gap: 12px;
  }
  .brand-dot {
    width: 14px;
    height: 14px;
    border-radius: 50%;
    background: var(--paper);
  }
  .brand-name {
    font-weight: 700;
    font-size: 38px;
    line-height: 1;
    color: var(--paper);
  }
  .product {
    position: absolute;
    top: 320px;
    left: 0;
    width: 540px;
    text-align: center;
  }
  .product-kicker {
    font-size: 14px;
    color: var(--crimson);
  }
  .product-name {
    margin-top: 36px;
    font-weight: 700;
    font-size: 72px;
    line-height: 1;
    color: var(--crimson);
  }
  .product-name sup {
    font-size: 52px;
    vertical-align: 28px;
    margin-left: 2px;
  }
  .product-ingredients {
    margin-top: 18px;
    font-weight: 700;
    font-size: 15px;
    color: var(--ink);
  }
  .pack-size {
    position: absolute;
    top: 560px;
    left: 0;
    width: 540px;
    text-align: center;
    font-weight: 700;
    font-size: 15px;
    letter-spacing: 1px;
    color: var(--paper);
  }
</style>
</head>
<body>
  <main class="label">
    <svg class="label-art" viewBox="0 0 540 600" aria-hidden="true">
      <rect x="0" y="0" width="540" height="600" fill="var(--crimson)"/>
      <path d="M60 40 C20 200, 20 400, 60 550 L480 550 C520 400, 520 200, 480 40 Z" fill="var(--leaf)"/>
      <path d="M74 40 C36 200, 36 400, 74 550 L466 550 C504 400, 504 200, 466 40 Z" fill="var(--paper)"/>
      <path d="M0 0 H540 V250 Q490 250 462 300 H78 Q50 250 0 250 Z" fill="var(--crimson)"/>
      <path d="M78 300 H462 Q490 250 540 250" fill="none" stroke="var(--leaf)" stroke-width="3"/>
      <path d="M0 250 Q50 250 78 300" fill="none" stroke="var(--leaf)" stroke-width="3"/>
      <path d="M0 540 H60 L80 525 H460 L480 540 H540 V600 H0 Z" fill="var(--crimson)"/>
    </svg>

    <header class="brand">
      <span class="brand-dot"></span>
      <span class="brand-name">Verdana Roots</span>
    </header>

    <section class="product">
      <p class="product-kicker">Daily Energy Booster</p>
      <h1 class="product-name">Vigor<sup>+</sup></h1>
      <p class="product-ingredients">(with ashwagandha, shilajit &amp; ginseng)</p>
    </section>

    <footer class="pack-size">Pack of 60 capsules</footer>
  </main>
</body>
</html>
```